"QuobbApps" Website Design

We are a new web/social media development company called "QuobbApps". We need a website homepage and 1 inner page designed. We want visitors to our site to know in the first few seconds that we design and build "apps". We do not want people leaving our homepage not having at least the high level understanding that we design and build "Apps".
We currently have a landing page up at www. quobbapps .com
We specialise in building bespoke
- Vexofon apps
- Drumlet apps
- Pindlerow Apps
- Korvath Apps
- Sunwhistle Apps
- Web applications
- Ulk Apps
- Social Media Marketing Solutions & Strategies
We need a website design concept that is clean, crisp, fresh and says the following about us...
We are a modern web 2.0 company (simple but striking/bold)
We are friendly, professional but dynamic and NOT boring
We are experts in developing apps
We are innovative, modern, energetic and funky
We deliver quality
We can develop to all budgets
The services we offer...
1. App Consultative Services
strategy and planning services for businesses who know they should have an "App" but dont know where to start or what type of App would achieve the best ROI in relation to their objectives.
2. Persona Driven Development leading to Solution & Requirement Design
We help the client understand their audience/target market by developing typical personas of the people who they want to use the app, these personas then drive the solution and the technical requirements. During this process we also pull together written technical specs that outlines the functionality of the app including any mandatory corporate requirements, plus screen-by-screen wireframes of their app with information about page transitions/navigation and any usability requiremens
3. App Design/User Experience Design
We develop a creative look and feel that delivers an outstanding user experience.
We develop Functional Design Specs showing the planned UI (User Interface) design, including the solution design and art direction following client sign off this is passed onto the development team to be programmed along with the apps features.
4. App Development
Turning the idea into a fully functional product with great UI and UX.
5. Maintenance
We offer a range of maintenance packages to suit all budgets, but give our clients piece of mind that there is always someone to call on when problems arise.
Our target audience is
1. anyone with an "App Idea" who needs to get from idea to production
and also
2. small and medium businesses and organisations.
PLEASE NOTE - We do not want a design churned out on an existing website template, so please dont waste your time if this is your normal design process, we will only consider bespoke design concepts that have really considered our brand and needs.
We expect to need additional pages designed which we will obviously look to offer the work to the designer who we choose in this competition.
Attached is a document containing links to websites with a mobile related theme that we like so you can get a feel for our likes and expectations, in addition we have attached our company logo for use in the design.
We dont have any photos or images to use, but are more than happy to pay for stockphotos etc. that are to be used in the final design.
We have not developed the text content or header titles yet so will need placeholder text/headers in place. Once we have the design we have the intention of working the content into the design and making it very search engine friendly, so we are happy for dummy text to be used in the design process unless you feel like making the text relevant.
Updates
Thanks for all the designs so far. General feedback relating to all designs...
Although nice, at present there isnt much "personality" in the designs and in most instances there is too much noise, could you please try and simplify the designs and reduce the amount of things for someone to look at but especially reduce the amount of text read.
3. Increase the amount of space
4. Be bolder with the use of the app brand logos
5. Maybe use more images of different well known smartphone handsets.
6. Vary the size of the typography more
7. Maybe try more vibrant colour combinations, especially with the text
Thanks and good luck
Hi there,
Just to add to the design concept ideas, ive had this image in my mind of the company logo somehow taking centre stage with all things "App" bursting out of it in a fun firework type of way (so smartphones, app brand logos, little square app icons etc.)
Not sure if this is a concept anyone want to attempt to pull something together on but trying to get away from the real "corporate" look. Apps are fun, exciting and interactive, i guess i want the website and the company to get that across about our company, but still get the message across that we are quality driven.
Thanks!
Target Market(s)
and also
Industry/Entity Type
Building
Requirements
Must have
- Clean
Crisp
Not too noisy, with space to breath and read without being overloaded by info.
4 or 5 persistant navigation links (e.g. About, Services, App Platforms, Contact Us, Blog)
The inner page needs to have a subtle contact form - this shouldnt be the focus of the page but just be a feature of it as we intend to have this as a feature on most of the inner pages. The contact form needs space to add info about project, and also a note stating that by submitting their idea we are automatically guaranteeing non disclosure.
Nice to have
- Other things the homepage and maybe the inner pages
A "Join our Pindlerow Fanpage"
A "Follow us on Plimber" link
A space for our plimber/blog/news feed
Should not have
- Should not be based on an off the shelf template layout

```html
<!DOCTYPE html>
<html lang="en">
<head>
<meta charset="utf-8">
<title>QuobbApps – About</title>
<link rel="stylesheet" href="https://fonts.googleapis.com/css2?family=Arimo:wght@400;700&family=Roboto+Condensed:wght@700&display=swap">
<style>
:root{
  --dark-1:#2b2d30;
  --dark-2:#4a4c50;
  --green:#22b51c;
  --green-light:#8fd80a;
  --lime:#7ccb2a;
  --ink:#111;
  --field:#dcdee0;
  --white:#fff;
  --btn:#5b5f64;
}
*{box-sizing:border-box;margin:0;padding:0}
html,body{width:1200px;height:1106px;overflow:hidden}
body{position:relative;font-family:"Arimo",Arial,sans-serif;color:var(--ink);background:var(--white)}
.cond{font-family:"Roboto Condensed","Arial Narrow",sans-serif;font-weight:700;letter-spacing:-.5px}

/* header */
.site-header{position:absolute;left:0;top:0;width:1200px;height:106px;background:linear-gradient(#2a2c2f,#55575b)}
.brand{position:absolute;left:62px;top:22px;text-align:center;color:var(--white)}
.brand-dot{width:64px;height:50px;border-radius:50%;background:var(--lime);margin:0 auto}
.brand-name{display:block;font-size:13px;font-weight:700;margin-top:3px}
.main-nav{position:absolute;left:519px;top:68px;display:flex;gap:0}
.main-nav a{color:var(--white);text-decoration:none;font-size:17px;margin-right:35px}
.main-nav a.current{color:var(--lime)}
.login{position:absolute;left:997px;top:66px;color:var(--white);font-size:17px}
.login-field{position:absolute;left:1050px;top:67px;width:112px;height:20px;background:var(--white);border-radius:3px}

/* intro */
.intro{position:absolute;left:0;top:106px;width:1200px;height:266px;background:linear-gradient(#fff 60%,#e6e6e6)}
.intro h1{position:absolute;left:62px;top:22px;font-size:29px;font-weight:400;letter-spacing:-.5px}
.intro-copy{position:absolute;left:59px;top:57px;width:388px;font-size:10px;line-height:13.5px;text-align:justify}
.intro-copy p+p{margin-top:13.5px}
.promo{position:absolute;left:897px;top:59px;width:260px;height:133px;background:var(--white);border-radius:12px;box-shadow:0 1px 6px rgba(0,0,0,.25)}
.promo-btn{position:absolute;left:32px;top:19px;width:198px;height:42px;border-radius:21px;background:linear-gradient(#6a6e73,#3d4044);color:var(--white);font-size:15px;line-height:42px;padding-left:36px}
.promo-btn svg{position:absolute;left:14px;top:14px}
.promo-text{position:absolute;left:35px;top:75px;font-size:12.5px;line-height:13.5px}
.promo-text span{color:var(--lime)}

/* green band */
.band{position:absolute;left:0;top:372px;width:1200px;height:660px;background:radial-gradient(ellipse 520px 360px at 200px 180px,var(--green-light),var(--green))}
.card{position:absolute;background:var(--white);border-radius:10px;box-shadow:0 1px 5px rgba(0,0,0,.25)}
.service{left:59px;width:384px;padding:12px 16px;font-size:9px;line-height:12.5px}
.service h2{font-size:19px;font-weight:400;letter-spacing:-.6px;line-height:20px}
.service p+h2{margin-top:12px}

.contact{left:464px;top:21px;width:385px;height:591px}
.contact h2{position:absolute;left:23px;top:18px;color:var(--lime);font-size:16px}
.field-label{position:absolute;font-size:12px;right:260px}
.field{position:absolute;left:136px;width:221px;height:20px;border-radius:10px;background:var(--field)}
.tell{position:absolute;left:76px;top:280px;width:281px;height:247px;border-radius:10px;background:var(--field)}
.form-btn{position:absolute;top:549px;height:24px;border-radius:12px;background:linear-gradient(#6a6e73,#3d4044);color:var(--white);font-size:12px;line-height:24px;text-align:center}

.scoop{position:absolute;left:899px;top:18px;width:250px;color:var(--ink);font-size:10px;line-height:13.5px;text-align:justify}
.scoop h2{color:var(--white);font-size:16px;line-height:18px}
.scoop article{margin-bottom:13.5px}
.scoop b{font-weight:700}
.scoop .lead{font-family:"Roboto Condensed","Arial Narrow",sans-serif;font-weight:700}

.follow{position:absolute;left:1063px;top:534px;color:var(--white)}
.follow h2{font-size:20px;font-family:"Arimo",Arial,sans-serif;font-weight:700;letter-spacing:-1px}
.follow ul{list-style:none;display:grid;grid-template-columns:repeat(2,auto);gap:3px 8px;margin-top:3px;font-size:8px;color:var(--white)}
.follow li{display:flex;align-items:center;gap:3px}
.follow li i{display:block;width:9px;height:9px;background:var(--white);border-radius:2px}

/* footer */
.site-footer{position:absolute;left:0;top:1032px;width:1200px;height:74px;background:linear-gradient(#4a4c50,#2b2d30);color:var(--white);font-size:9px}
.footer-dot{position:absolute;left:46px;top:18px;width:40px;height:32px;border-radius:50%;background:var(--lime)}
.footer-legal{position:absolute;left:95px;top:30px}
.footer-nav{position:absolute;left:318px;top:30px}
.footer-nav span{margin:0 19px}
</style>
</head>
<body>

<header class="site-header">
  <div class="brand"><div class="brand-dot"></div><span class="brand-name">QuobbApps</span></div>
  <nav class="main-nav cond">
    <a href="#">HOME</a><a href="#" class="current">ABOUT</a><a href="#" style="margin-right:43px">NEWS</a><a href="#" style="margin-right:38px">HELP</a><a href="#">DOWNLOAD</a>
  </nav>
  <div class="login">Login</div>
  <div class="login-field"></div>
</header>

<section class="intro">
  <h1>About Us</h1>
  <div class="intro-copy">
    <p>Contrary to popular belief, Lorem Ipsum is not simply random text. It has roots in a piece of classical Latin literature from 45 BC, making it over 2000 years old. Tobin Ashcroft, a Latin professor at Marrowby College in Virginia, looked up one of the more obscure Latin words, consectetur, from a Lorem Ipsum passage, and going through the cites of the word in classical literature, discovered the undoubtable source. Lorem Ipsum comes from sections 1.10.32 and 1.10.33 of "de Finibus Bonorum et Malorum" (The Extremes of Good and Evil) by Verdanus, written in 45 BC.</p>
    <p>This book is a treatise on the theory of ethics, very popular during the Renaissance. through the cites of the word in classical literature, discovered the undoubtable source. Lorem Ipsum comes from sections 1.10.32 and 1.10.33 of "de Finibus Bonorum et Malorum" (The Extremes of Good and Evil) by Verdanus, written in 45 BC. This book is a treatise on the theory of ethics, very popular during the Renaissance. The first line of Lorem Ipsum, "Lorem ipsum dolor</p>
  </div>
  <aside class="promo">
    <div class="promo-btn cond">
      <svg width="14" height="12" viewBox="0 0 14 12"><path d="M1 3l6 6 6-6" fill="none" stroke="#fff" stroke-width="2.5"/></svg>
      GET A FREE VEXOFON APP
    </div>
    <p class="promo-text">Get the free Vexofon app<br><span>Sign up to hear</span> about future<br>product improvements.</p>
  </aside>
</section>

<section class="band">
  <div class="card service" style="top:21px;height:86px">
    <h2>App Consultative Services</h2>
    <p>strategy and planning services for businesses who know they should have an "App" but dont know where to start or what type of App would achieve the best ROI in relation to their objectives</p>
  </div>
  <div class="card service" style="top:137px;height:85px">
    <h2>App Development</h2>
    <p>Turning the idea into a fully functional product with great UI and UX.</p>
  </div>
  <div class="card service" style="top:251px;height:131px;padding-left:12px">
    <h2>App Design/User Experience Design</h2>
    <p>We develop a creative look and feel that delivers an outstanding user experience.</p>
    <p style="margin-top:12.5px">We develop Functional Design Specs showing the planned UI (User Interface) design, including the solution design and art direction following client sign off this is passed onto the development team to be programmed along with the apps features.</p>
  </div>
  <div class="card service" style="top:407px;height:203px;padding-left:14px">
    <h2>Persona Driven Development leading to<br>Solution &amp; Requirement Design</h2>
    <p>We help the client understand their audience/target market by developing typical personas of the people who they want to use the app, these personas then drive the solution and the technical requirements. During this process we also pull together written technical specs that outlines the functionality of the app including any mandatory corporate requirements, plus screen-by-screen wireframes of their app with information about page transitions/navigation and any usability requirements</p>
    <h2>Maintenance</h2>
    <p>We offer a range of maintenance packages to suit all budgets, but give our clients piece of mind that there is always someone to call on when problems arise. .</p>
  </div>

  <form class="card contact cond">
    <h2>CONTACT US</h2>
    <span class="field-label" style="top:59px">NAME</span><span class="field" style="top:55px"></span>
    <span class="field-label" style="top:95px">SURNAME</span><span class="field" style="top:91px"></span>
    <span class="field-label" style="top:131px">PHONE</span><span class="field" style="top:127px"></span>
    <span class="field-label" style="top:166px">ADRESS</span><span class="field" style="top:162px"></span>
    <span class="field-label" style="top:206px">COMPANY</span><span class="field" style="top:203px"></span>
    <span class="field-label" style="top:246px">CELLULAR</span><span class="field" style="top:243px"></span>
    <span class="field-label" style="top:281px;right:316px">TELL US</span><span class="tell"></span>
    <span class="form-btn" style="left:222px;width:60px">RESET</span>
    <span class="form-btn" style="left:291px;width:62px">SUBMIT</span>
  </form>

  <div class="scoop">
    <h2 class="cond">LATEST SCOOP</h2>
    <article><span class="lead">06/24/10 How to Make the Most of Your Vexofon 4 Lumo (Free): This digital assistant is surprisingly slick.</span> Open the app and use your voice to…</article>
    <article><span class="lead">04/28/10 Orchard Buys a Start-Up for Its Voice Technology</span><br>For example, Lumo users can speak commands like “find a table for two at 9 tonight”…</article>
    <article><span class="lead">04/28/10 What Orchard’s Acquisition of Lumo Means for the Future of Mobile Search</span><br>What Lumo does is quite brilliant. Because it uses natural voice search for its queries, it’s…</article>
    <article><span class="lead">04/28/10 Orchard Moves Deeper Into Voice-Activated Search With Lumo Buy</span><br>Lumo’s free app is connected to a whole ecosystem of Web services and programming interfaces, and…</article>
    <article><span class="lead">04/21/10 Ned Harrowgate On The Future Of Search: Part Two</span><br>One of the poster child apps that’s shaking up the current status quo is Lumo, an…</article>
  </div>

  <div class="follow">
    <h2>FollowUs</h2>
    <ul>
      <li><i></i>Pindlerow</li><li><i></i>Plimber</li>
      <li><i></i>Vidcaddy</li><li><i></i>Snapwhorl</li>
      <li><i></i>Tumblewick</li>
    </ul>
  </div>
</section>

<footer class="site-footer">
  <div class="footer-dot"></div>
  <div class="footer-legal">© 2010 All rights reserved &nbsp;| &nbsp;Privacy Policy</div>
  <nav class="footer-nav">Home<span>|</span>About<span>|</span>News<span>|</span>Help<span>|</span>Download</nav>
</footer>

</body>
</html>
```